Business Card & Stationary Design Project

We are looking for some creative direction for business cards and our stationary.

We are a global logistics firm that has recently changed its name to Marrick Global Logistics and we have a new website due out tomorrow (www.marrick.com.au).

The colours of the company are rich navy tones, I would like to have business cards that fit together to make one picture on the back (possibly an old map of the world??), and the front to be modern contemporary looking.

But I am open to suggestions, so just incorporate our new logo and get going!
Updates

Hi Everyone,

Thank you for all of your designs so far and the time you have put into it.

I have asked many of you for amendments to see if we can get a final product, so with this in mind I am extending the deadline by a few days.

Good luck and thank you once again.

Please message me direct if you need any clarification.

Kind Regards
Colin

Reason: As outlined the extra 3 days is for amendments and changes to the current submissions. Thanks Colin

Industry/Entity Type

Business

```html
<!DOCTYPE html>
<html lang="en">
<head>
<meta charset="utf-8">
<title>Marrick Global Logistics – Business Card</title>
<link rel="stylesheet" href="https://fonts.googleapis.com/css2?family=Montserrat:wght@700&family=Questrial&display=swap">
<style>
  :root {
    --backdrop: #e6eaf0;
    --paper: #fbfbfa;
    --navy: #0d2f66;
    --navy-deep: #092450;
    --sky: #3b8fe0;
    --sky-soft: #5aa6ee;
    --ink: #12306a;
    --text-light: #dbe8f8;
    --shadow: rgba(9, 36, 80, 0.22);
  }
  * { box-sizing: border-box; margin: 0; padding: 0; }
  html, body { width: 1200px; height: 800px; overflow: hidden; }
  body {
    background: var(--backdrop);
    font-family: "Questrial", "Century Gothic", sans-serif;
    color: var(--ink);
    position: relative;
  }
  .card {
    position: absolute;
    top: 240px;
    width: 540px;
    height: 320px;
    border-radius: 4px;
    overflow: hidden;
    box-shadow: 0 14px 34px var(--shadow);
  }
  .card--front { left: 40px; background: var(--paper); }
  .card--back { left: 620px; }

  /* Logo lockup */
  .wordmark {
    position: absolute;
    font-family: "Questrial", "Century Gothic", sans-serif;
    color: var(--navy);
    line-height: 1;
  }
  .wordmark__name { display: block; font-size: 52px; letter-spacing: 15px; }
  .wordmark__tag { display: block; font-size: 15px; letter-spacing: 8.4px; margin-top: 8px; }
  .card--front .wordmark { left: 38px; top: 48px; }
  .badge-dot {
    position: absolute;
    width: 58px; height: 58px;
    border-radius: 50%;
    background: var(--sky);
  }
  .card--front .badge-dot { right: 34px; top: 30px; }

  /* Person */
  .person { position: absolute; left: 40px; top: 176px; }
  .person__name {
    font-family: "Montserrat", "Century Gothic", sans-serif;
    font-weight: 700;
    font-size: 19px;
    letter-spacing: 0.3px;
    color: var(--navy);
  }
  .person__role { font-size: 15px; color: var(--sky); margin-top: 4px; }

  .address {
    position: absolute; left: 262px; top: 150px;
    font-size: 14px; line-height: 22px; color: var(--navy);
  }
  .address__line { display: flex; align-items: center; gap: 8px; }

  /* Lower band */
  .band { position: absolute; left: 0; top: 0; width: 540px; height: 320px; }
  .band__map {
    position: absolute; right: 0; top: 196px;
    width: 300px; height: 124px;
    background: radial-gradient(ellipse at 55% 45%, rgba(90,150,220,0.28), rgba(13,47,102,0) 70%);
  }
  .contact {
    position: absolute;
    font-size: 14.5px; line-height: 26px; color: var(--text-light);
  }
  .contact--phones { left: 62px; top: 250px; }
  .contact--web { left: 290px; top: 226px; }
  .contact__row { display: flex; align-items: center; gap: 10px; }
  .icon { width: 16px; height: 16px; flex: none; }

  /* Back */
  .back-field {
    position: absolute; inset: 0;
    background:
      radial-gradient(ellipse at 60% 55%, rgba(120,180,240,0.35), rgba(0,0,0,0) 65%),
      linear-gradient(135deg, var(--navy-deep) 0%, #1f5fae 55%, var(--sky-soft) 100%);
  }
  .card--back .wordmark { color: #f2f5fa; left: 40px; top: 118px; }
  .card--back .badge-dot { right: 36px; top: 90px; background: #cfe3f7; }
</style>
</head>
<body>
  <section class="card card--front" aria-label="Business card front">
    <div class="wordmark">
      <span class="wordmark__name">MARRICK</span>
      <span class="wordmark__tag">GLOBAL LOGISTICS</span>
    </div>
    <span class="badge-dot"></span>

    <div class="person">
      <p class="person__name">COLIN ASHBY</p>
      <p class="person__role">General Manager</p>
    </div>

    <div class="address">
      <p class="address__line">87 Harbour Row, Eastbay</p>
      <p class="address__line">NSW 2061
        <svg class="icon" viewBox="0 0 16 16" aria-hidden="true"><circle cx="8" cy="8" r="7.2" fill="none" stroke="#3b8fe0" stroke-width="1.2"/><rect x="4.5" y="6.5" width="7" height="4" fill="none" stroke="#3b8fe0" stroke-width="1.1"/><rect x="5.8" y="4.3" width="4.4" height="2.2" fill="#3b8fe0"/></svg>
        02 9100 4417</p>
    </div>

    <svg class="band" viewBox="0 0 540 320" aria-hidden="true">
      <polygon points="0,228 540,188 540,202 0,242" fill="#3b8fe0"/>
      <polygon points="0,242 540,202 540,320 0,320" fill="#0d2f66"/>
    </svg>
    <div class="band__map" role="img" aria-label="Faint dotted world map across the lower band"></div>

    <div class="contact contact--phones">
      <p class="contact__row">
        <svg class="icon" viewBox="0 0 16 16" aria-hidden="true"><circle cx="8" cy="8" r="7.2" fill="none" stroke="#5aa6ee" stroke-width="1.2"/><path d="M5.4 4.4l1.4-.2.8 1.9-.9.7a5 5 0 0 0 2.5 2.5l.7-.9 1.9.8-.2 1.4c-3.4.3-6.5-2.8-6.2-6.2z" fill="#5aa6ee"/></svg>
        02 8100 4400</p>
      <p class="contact__row">
        <svg class="icon" viewBox="0 0 16 16" aria-hidden="true"><circle cx="8" cy="8" r="7.2" fill="none" stroke="#5aa6ee" stroke-width="1.2"/><rect x="4.5" y="6.5" width="7" height="4" fill="none" stroke="#5aa6ee" stroke-width="1.1"/><rect x="5.8" y="4.3" width="4.4" height="2.2" fill="#5aa6ee"/></svg>
        02 9100 4417</p>
    </div>

    <div class="contact contact--web">
      <p class="contact__row">
        <svg class="icon" viewBox="0 0 16 16" aria-hidden="true"><circle cx="8" cy="8" r="7.2" fill="none" stroke="#5aa6ee" stroke-width="1.2"/><rect x="4.3" y="5.3" width="7.4" height="5.4" fill="none" stroke="#5aa6ee" stroke-width="1"/><path d="M4.3 5.3L8 8.3l3.7-3" fill="none" stroke="#5aa6ee" stroke-width="1"/></svg>
        colin@marrick.com.au</p>
      <p class="contact__row">
        <svg class="icon" viewBox="0 0 16 16" aria-hidden="true"><circle cx="8" cy="8" r="7.2" fill="none" stroke="#5aa6ee" stroke-width="1.2"/><circle cx="8" cy="8" r="4.2" fill="none" stroke="#5aa6ee" stroke-width="0.9"/><ellipse cx="8" cy="8" rx="1.8" ry="4.2" fill="none" stroke="#5aa6ee" stroke-width="0.9"/><path d="M3.8 8h8.4" stroke="#5aa6ee" stroke-width="0.9"/></svg>
        www.marrick.com.au</p>
    </div>
  </section>

  <section class="card card--back" aria-label="Business card back">
    <div class="back-field" role="img" aria-label="Dotted world map in rich navy and blue tones, continuing across the set of cards"></div>
    <div class="wordmark">
      <span class="wordmark__name">MARRICK</span>
      <span class="wordmark__tag">GLOBAL LOGISTICS</span>
    </div>
    <span class="badge-dot"></span>
  </section>
</body>
</html>
```